Realty Group Needs Classy, Contemporary Letterhead Design

We need a letterhead design for a new realty company located in NY, USA. We buy investment properties to rehabilitate and or keep in our rental portfolio.

```html
<!DOCTYPE html>
<html lang="en">
<head>
<meta charset="UTF-8">
<title>Halvern Realty Group — Letterhead</title>
<link href="https://fonts.googleapis.com/css2?family=Source+Sans+3:wght@400;700;800&display=swap" rel="stylesheet">
<style>
  :root {
    --backdrop: #5a5a5c;
    --paper: #ffffff;
    --brand-purple: #4f2d86;
    --band-gray: #7d7d7d;
    --body-text: #8c8c8c;
    --footer-text: #444444;
    --rule: #9a9a9a;
  }
  * { margin: 0; padding: 0; box-sizing: border-box; }
  html, body {
    width: 960px; height: 1200px; overflow: hidden;
    background: var(--backdrop);
    font-family: "Source Sans 3", sans-serif;
  }
  .letterhead {
    position: absolute; left: 98px; top: 61px;
    width: 762px; height: 1078px;
    background: var(--paper);
    overflow: hidden;
  }
  .brand-name {
    position: absolute; left: 50px; top: 86px;
    font-family: "Source Sans 3", sans-serif;
    font-weight: 800; font-size: 24px; letter-spacing: 0.5px;
    color: var(--brand-purple);
  }
  .salutation {
    position: absolute; left: 67px; top: 250px;
    font-size: 14.5px; color: var(--body-text);
  }
  .letter-body {
    position: absolute; left: 50px; top: 314px; width: 685px;
    font-size: 14.6px; line-height: 18.4px;
    color: var(--body-text); text-align: justify;
  }
  .letter-body p + p { margin-top: 18.4px; }
  .letter-body p:first-child { text-indent: 46px; }
  .contact {
    position: absolute; top: 1015px;
    font-size: 12px; line-height: 15.3px; color: var(--footer-text);
  }
  .contact-address { left: 66px; }
  .contact-phone { left: 342px; }
  .contact-icon { position: absolute; }
  .contact-divider {
    position: absolute; left: 255px; top: 1006px;
    width: 1px; height: 39px; background: var(--rule);
  }
  .footer-band { position: absolute; left: 0; top: 1030px; }
  .website {
    position: absolute; left: 615px; top: 1040px;
    font-size: 12px; color: #ffffff;
  }
  .website-icon { position: absolute; left: 598px; top: 1044px; }
</style>
</head>
<body>
  <main class="letterhead">
    <div class="brand-name">HALVERN REALTY GROUP, LLC</div>

    <div class="salutation">Dear Sir</div>

    <section class="letter-body">
      <p>Lorem ipsum dolor sit amet, consectetur adipiscing elit. Integer eu odio mattis, pulvinar turpis quis, faucibus nisl. Proin feugiat, erat vitae cursus pharetra, enim est semper ligula, in malesuada orci nisl et diam. Etiam elementum metus ac fringilla vulputate. Etiam mattis ligula sed ante mollis bibendum. Orci varius natoque penatibus et magnis dis parturient montes, nascetur ridiculus mus.</p>
      <p>Ut nibh augue, blandit ac orci ac, rutrum congue enim. Suspendisse gravida vulputate felis, quis interdum orci tincidunt quis. Praesent imperdiet maximus neque. Mauris ut dui enim. Nullam at efficitur elit. Donec ante ipsum, fermentum at lectus vel, blandit vulputate ante. Proin luctus suscipit diam id vestibulum. Morbi malesuada id mauris eget ullamcorper.</p>
      <p>Donec varius orci purus, vitae aliquam libero volutpat id. Integer sed imperdiet libero. Aliquam accumsan, risus sit amet ornare consectetur, turpis felis dictum justo, non rhoncus mauris dui sed velit. Pellentesque habitant morbi tristique senectus et netus et malesuada fames ac turpis egestas. Pellentesque tincidunt vitae ligula nec imperdiet. Donec sed congue enim. Nullam elementum faucibus nulla nec vestibulum. Sed at tempor ligula. In quis vulputate nunc. Integer at gravida lacus, ac tristique risus. Sed at vulputate nulla.</p>
      <p>Praesent blandit nunc eu efficitur commodo. In tempor nisi ex, vel venenatis ante vestibulum a. Duis vestibulum nibh a erat sagittis, nec euismod lorem varius. Nam ultricies turpis sed justo sollicitudin volutpat. Morbi sed mollis eros. Sed quis tortor id enim vehicula porttitor. Curabitur non aliquam ex. Phasellus dignissim fermentum elit, at finibus ligula mattis eget.</p>
    </section>

    <svg class="contact-icon" style="left:49px;top:1014px" width="11" height="15" viewBox="0 0 11 15" aria-hidden="true">
      <path d="M5.5 0.5a5 5 0 0 1 5 5c0 3.5-5 9-5 9s-5-5.5-5-9a5 5 0 0 1 5-5z" fill="#444"/>
      <circle cx="5.5" cy="5.5" r="2" fill="#fff"/>
    </svg>
    <div class="contact contact-address">suit # 00, Lorem ipsum<br>Lorem Lorem ipsum</div>

    <div class="contact-divider"></div>

    <svg class="contact-icon" style="left:323px;top:1017px" width="12" height="12" viewBox="0 0 12 12" aria-hidden="true">
      <path d="M2.5 0.8l2 2.4-1.2 1.5c.8 1.7 2.2 3.1 3.9 3.9l1.5-1.2 2.4 2-1.4 2C5 11 1 7 .7 2.2z" fill="#444"/>
    </svg>
    <svg class="contact-icon" style="left:323px;top:1032px" width="12" height="11" viewBox="0 0 12 11" aria-hidden="true">
      <path d="M0 4l6-4 6 4v7H0z" fill="#444"/>
      <path d="M1 4.5l5 3.2 5-3.2" stroke="#fff" stroke-width="1" fill="none"/>
    </svg>
    <div class="contact contact-phone">000-000-0000<br>000-000-0000</div>

    <svg class="footer-band" width="762" height="48" viewBox="0 0 762 48" aria-hidden="true">
      <rect x="0" y="21" width="500" height="27" fill="var(--band-gray)"/>
      <polygon points="500,0 762,0 762,48 475,48" fill="var(--brand-purple)"/>
    </svg>
    <svg class="website-icon" width="11" height="11" viewBox="0 0 11 11" aria-hidden="true">
      <g fill="none" stroke="#fff" stroke-width="0.9">
        <circle cx="5.5" cy="5.5" r="4.8"/>
        <ellipse cx="5.5" cy="5.5" rx="2.2" ry="4.8"/>
        <line x1="0.7" y1="5.5" x2="10.3" y2="5.5"/>
      </g>
    </svg>
    <div class="website">www.halvernrealty.com</div>
  </main>
</body>
</html>
```